Zielgruppe
Ich biete Marketing und Beratung an. Meine Zielgruppe sind KMU's aber auch Einzelfirmen welche selbst keine Marketingabteilung haben.
Aufgabenstellung
Sie sollen mein bestehendes CI/CD von meiner Website www.velorusk.ch möglichst mit Farben, Formen und Schriften übernehmen. Es soll eine einfache Seite mit 3 Rubriken werden. Über mich / Mein Angebot (Philosophie, Schwerpunkte/Preise) / Kontakt. Impressum, AGB und Datenschutz sollen CH Konform integriert sein. Ich habe meine Domain bei serwanox.ch registriert. Diese soll dann für die neue Website eingerichtet werden und von der Pixolo Seite entfernt werden. Der Link für Kontrabu soll funktionieren. Bilder können von der Pixolo Seite entnommen werden. Da ich für meine Kunden viele Websiten erstellen lassen werde, suche ich einen Designer*in mit welcher ich auch nach dieser Website zusammen arbeiten könnte. Die Seite möchte ich danach selber pflegen können. Es wäre toll wenn sie mit Wordpress erstellt wird (muss aber nicht sein).

```html
<!DOCTYPE html>
<html lang="de">
<head>
<meta charset="utf-8">
<title>Velorusk – Marketing &amp; Beratung</title>
<link href="https://fonts.googleapis.com/css2?family=Montserrat:wght@500;600;700;800&family=Inter:wght@400;500;600&display=swap" rel="stylesheet">
<style>
:root{
  --green:#1f8a4c;
  --green-soft:#e8f5ee;
  --mint:#eef8f3;
  --ink:#141414;
  --dark:#191919;
  --card-dark:#222;
  --line:#e6e6e6;
  --muted:#666;
  --muted-dark:#8a8a8a;
}
*{box-sizing:border-box;margin:0;padding:0}
html,body{width:1200px;height:4212px;overflow:hidden}
body{font-family:"Inter",sans-serif;color:var(--ink);background:#fff;position:relative}
h1,h2,h3,.head{font-family:"Montserrat",sans-serif}
section,header,footer{position:absolute;left:0;width:1200px}
.abs{position:absolute}

/* Nav */
.nav{top:0;height:66px;border-bottom:1px solid #f0f0f0;background:#fff}
.brand{left:100px;top:8px;font-family:"Montserrat",sans-serif;font-weight:700;font-size:38px;letter-spacing:-1px;color:var(--ink)}
.brand small{display:block;font-size:8px;letter-spacing:.5px;font-weight:500;margin:-8px 0 0 74px;color:#555}
.menu{right:87px;top:18px;display:flex;gap:24px;align-items:center;font-size:11px;font-weight:600;font-family:"Montserrat",sans-serif}
.btn-pill{background:var(--green);color:#fff;padding:9px 20px;border-radius:20px}

/* Hero */
.hero{top:66px;height:554px;background:linear-gradient(90deg,#fff 0%,#fff 40%,var(--mint) 100%)}
.tag{left:87px;top:64px;border:1px solid #dfe9e3;border-radius:14px;padding:5px 10px;font-size:9px;font-weight:700;color:var(--green);letter-spacing:.5px;font-family:"Montserrat",sans-serif}
.tag::before{content:"";display:inline-block;width:6px;height:6px;border-radius:50%;background:var(--green);margin-right:8px;vertical-align:1px}
.hero h1{left:87px;top:115px;font-size:58px;line-height:60px;font-weight:800;letter-spacing:-1px}
.hero h1 .g{color:var(--green)}
.hero-lead{left:87px;top:324px;width:420px;font-size:16px;line-height:27px;color:#555}
.hero-cta{left:87px;top:416px;display:flex;gap:14px}
.btn{font-size:13px;font-weight:600;padding:15px 26px;border-radius:6px}
.btn.fill{background:var(--green);color:#fff}
.btn.ghost{background:#fff;border:1px solid var(--line)}
.hero-card{left:620px;top:14px;width:493px;height:500px;background:#fff;border-radius:18px;box-shadow:0 10px 40px rgba(0,0,0,.08)}
.portrait{left:160px;top:60px;width:150px;height:300px;background:linear-gradient(180deg,#d9d9d9,#555 70%,#2a2a2a);border-radius:70px 70px 8px 8px}
.mini-ico{width:46px;height:46px;border-radius:10px;background:#eee;left:68px}
.verified{left:340px;top:200px;width:108px;height:102px;background:#fff;border-radius:12px;box-shadow:0 8px 24px rgba(0,0,0,.1);text-align:center;font-size:12px;font-weight:700;padding-top:18px}
.verified i{display:block;width:36px;height:36px;margin:0 auto 8px;border-radius:50%;background:#999}
.verified span{display:block;font-size:7px;font-weight:400;color:#777;margin-top:2px}
.chart{left:110px;top:390px;width:260px;height:100px}
.chart-lbl{left:125px;top:393px;font-size:11px;font-weight:600}
.toggle{left:285px;top:395px;font-size:6px;color:#777}
.expert{left:260px;top:410px;width:200px;height:60px;background:#fff;border-radius:10px;box-shadow:0 6px 20px rgba(0,0,0,.1);display:flex;align-items:center;gap:12px;padding:0 14px}
.expert .av{width:34px;height:34px;border-radius:50%;background:var(--green);color:#fff;font-size:11px;font-weight:700;display:flex;align-items:center;justify-content:center}
.expert small{display:block;font-size:8px;color:#888;letter-spacing:.5px}
.expert b{font-size:12px}

/* Philosophy */
.philo{top:620px;height:845px;background:#fff}
.center{left:0;width:1200px;text-align:center}
.philo h2{top:98px;font-size:40px;font-weight:700}
.sub{top:160px;font-size:14px;font-weight:600;letter-spacing:2px;color:#555;font-family:"Montserrat",sans-serif}
.pcards{left:247px;top:237px;display:flex;gap:28px}
.pcard{width:217px;height:181px;border-radius:16px;border:1px solid #eee;box-shadow:0 8px 24px rgba(0,0,0,.06);text-align:center;padding-top:34px;position:relative;overflow:hidden;background:#fff}
.pcard h3{position:relative;z-index:1;color:var(--green);font-size:24px;font-weight:800}
.pcard p{position:relative;z-index:1;font-size:15px;line-height:23px;margin-top:6px}
.pcard .deco{position:absolute;right:12px;top:14px;width:56px;height:56px;border:3px solid #f1f1f1;border-radius:12px;z-index:0}
.quote{top:495px;font-family:"Montserrat",sans-serif;font-size:24px;line-height:31px;font-weight:500;color:#333}
.qmark{left:248px;top:465px;font-size:60px;color:#ddd;font-family:Georgia,serif}
.author{top:585px;font-size:13px;font-weight:600;color:var(--green);letter-spacing:1px}
.author::before,.author::after{content:"";display:inline-block;width:40px;height:1px;background:var(--green);vertical-align:4px;margin:0 16px}
.arc{left:247px;top:683px}

/* Focus */
.focus{top:1465px;height:820px;background:var(--dark);color:#fff}
.focus .bar{left:87px;top:140px;width:52px;height:5px;background:var(--green)}
.focus h2{left:87px;top:170px;font-size:34px;line-height:36px;font-weight:800}
.focus h2 span{color:var(--green)}
.focus .lead{left:87px;top:264px;width:320px;font-size:16px;line-height:27px;color:#bbb}
.focus .link{left:87px;top:400px;font-size:13px;color:var(--green);font-weight:600;border-bottom:2px solid var(--green);padding-bottom:3px}
.grid{left:472px;top:106px;display:grid;grid-template-columns:311px 311px;gap:20px 20px}
.fcard{height:188px;background:var(--card-dark);border:1px solid #333;border-radius:10px;padding:26px 28px}
.fcard .ic{width:42px;height:42px;border-radius:8px;background:#333;display:flex;align-items:center;justify-content:center}
.fcard h3{font-size:20px;font-weight:700;margin-top:24px}
.fcard p{font-size:11px;line-height:17px;color:var(--muted-dark);margin-top:10px;width:250px}
.wave{left:0;bottom:0}

/* Prices */
.prices{top:2284px;height:786px;background:var(--mint)}
.prices h2{top:102px;font-size:40px;font-weight:800}
.prices .rule{left:570px;top:165px;width:60px;height:4px;background:var(--green)}
.prices .lead{top:195px;font-size:14px;line-height:24px;color:#555}
.plan{top:303px;width:413px;height:376px;border-radius:16px;padding:34px 34px}
.plan.light{left:173px;background:#fff;box-shadow:0 10px 30px rgba(0,0,0,.06)}
.plan.dark{left:613px;background:var(--dark);color:#fff;box-shadow:0 14px 34px rgba(0,0,0,.25)}
.plan .top{display:flex;justify-content:space-between;align-items:baseline;padding-bottom:24px;border-bottom:1px solid #eee}
.plan.dark .top{border-color:#333}
.plan h3{font-size:20px;font-weight:700}
.plan .price{font-size:30px;color:var(--green);font-weight:600}
.plan .price small{font-size:13px;color:#888;margin-left:4px}
.plan .pill{display:inline-block;margin-top:8px;font-size:9px;font-weight:700;letter-spacing:1px;padding:4px 8px;background:#f2f2f2;color:#777;border-radius:3px}
.plan.dark .pill{background:#333;color:#aaa}
.plan ul{list-style:none;margin-top:26px}
.plan li{font-size:13px;line-height:33px;display:flex;align-items:center;gap:14px}
.plan li i{width:15px;height:15px;border-radius:50%;background:#e7f2eb;display:inline-flex;align-items:center;justify-content:center}
.plan.dark li i{background:var(--green)}
.plan .cta{margin-top:32px;display:block;text-align:center;font-size:12px;font-weight:700;letter-spacing:1px;padding:14px;border-radius:6px;color:var(--green);border:2px solid var(--green)}
.plan.dark .cta{background:var(--green);color:#fff}

/* Contact */
.contact{top:3070px;height:780px;background:#fff}
.contact h2{left:87px;top:105px;font-size:40px;font-weight:800}
.contact .rule{left:87px;top:168px;width:66px;height:4px;background:var(--green)}
.contact .lead{left:87px;top:196px;width:470px;font-size:16px;line-height:27px;color:#555}
.info{left:87px;display:flex;gap:22px}
.info .ic{width:48px;height:48px;border-radius:10px;background:var(--green-soft);display:flex;align-items:center;justify-content:center}
.info b{font-family:"Montserrat",sans-serif;font-size:15px;display:block;margin-bottom:4px}
.info span{font-size:14px;line-height:21px;color:#555}
.me{left:87px;top:592px;width:80px;height:80px;border-radius:50%;border:3px solid var(--green);background:linear-gradient(135deg,#e6e6e6,#9a9a9a)}
.soc{width:32px;height:32px;border-radius:50%;background:var(--ink)}
.note{left:193px;top:644px;font-size:11px;font-style:italic;color:#666}
.form{left:628px;top:107px;width:485px;height:526px;border-radius:16px;box-shadow:0 10px 36px rgba(0,0,0,.07);padding:38px 40px}
.form h3{font-size:20px;font-weight:700;margin-bottom:26px}
.field{border:1px solid var(--line);border-radius:4px;height:48px;font-size:13px;color:#999;padding:14px;background:#fff}
.row{display:flex;gap:20px;margin-bottom:20px}
.row .field{flex:1}
.consent{display:flex;gap:10px;font-size:11px;line-height:16px;color:#666;margin:18px 0 26px}
.consent i{width:12px;height:12px;border:1px solid #999;margin-top:3px;flex:none}
.send{background:var(--green);color:#fff;border-radius:6px;text-align:center;padding:17px;font-size:14px;font-weight:600}

/* Footer */
.foot{top:3850px;height:362px;background:var(--dark);color:#bbb}
.foot .logo{left:92px;top:68px;font-family:"Montserrat",sans-serif;font-weight:700;font-size:26px;color:#fff;letter-spacing:-.5px}
.foot .about{left:87px;top:120px;width:330px;font-size:13px;line-height:22px}
.foot h4{font-family:"Montserrat",sans-serif;font-size:14px;color:#fff;font-weight:700}
.foot ul{list-style:none;margin-top:24px;font-size:13px;line-height:30px}
.foot li::before{content:"› ";color:var(--green)}
.foot .socs{display:flex;gap:12px;margin-top:22px}
.foot .socs i{width:38px;height:38px;border-radius:50%;background:#2c2c2c;display:block}
.foot .base{left:87px;top:268px;width:1026px;border-top:1px solid #2c2c2c;padding-top:18px;display:flex;justify-content:space-between;font-size:11px;color:#777}
</style>
</head>
<body>

<header class="nav">
  <div class="abs brand">velorusk<small>MARKETING &amp; BERATUNG</small></div>
  <nav class="abs menu"><span>ÜBER MICH</span><span>ANGEBOT</span><span>PREISE</span><span class="btn-pill">Kontakt</span></nav>
</header>

<section class="hero">
  <div class="abs tag">DEIN MARKETING PROFI</div>
  <h1 class="abs">KLAR.<br><span class="g">INSPIRIEREND.</span><br>WIRKSAM.</h1>
  <p class="abs hero-lead">Durch meine Marketing Expertise hole ich das Beste aus Ihrem Unternehmen heraus.</p>
  <div class="abs hero-cta">
    <span class="btn fill">Kostenlose Offerte verlangen &nbsp;→</span>
    <span class="btn ghost">◈ &nbsp;Mein Angebot</span>
  </div>
  <div class="abs hero-card">
    <svg class="abs" style="left:0;top:0" width="493" height="500" fill="none" stroke="#e2e2e2" stroke-width="1.5">
      <path d="M91 130 V390 H230"/><path d="M310 145 H390 V200"/>
    </svg>
    <div class="abs mini-ico" style="top:165px"></div>
    <div class="abs mini-ico" style="top:225px"></div>
    <div class="abs portrait" role="img" aria-label="Porträtfoto der Beraterin, schwarz-weiss"></div>
    <div class="abs verified"><i></i>Verified!<span>100% Client Satisfied</span></div>
    <div class="abs chart-lbl">B2B Income 2025</div>
    <div class="abs toggle">Monthly / Yearly</div>
    <svg class="abs chart" viewBox="0 0 260 100" fill="none"><path d="M20 90 L60 70 L90 78 L130 50 L170 55" stroke="#888" stroke-width="1.5"/></svg>
    <div class="abs expert"><div class="av">MJ</div><div><small>EXPERTISE</small><b>15+ Jahre Erfahrung</b></div></div>
  </div>
</section>

<section class="philo">
  <h2 class="abs center">MEINE PHILOSOPHIE</h2>
  <div class="abs center sub">WAS STEHT HINTER VELORUSK..?</div>
  <div class="abs pcards">
    <div class="pcard"><span class="deco"></span><h3>VELO</h3><p>Branding</p></div>
    <div class="pcard"><span class="deco"></span><h3>VELOR</h3><p>Business</p></div>
    <div class="pcard"><span class="deco"></span><h3>RUSK</h3><p>Erzeugen<br>Erneuern<br>Kreieren</p></div>
  </div>
  <div class="abs qmark">“</div>
  <p class="abs center quote">Durch meine Marketing Expertise hole ich das<br>Beste aus Ihrem Unternehmen heraus.</p>
  <div class="abs center author">MIRELKA JOST</div>
  <svg class="abs arc" width="706" height="54" viewBox="0 0 706 54"><path d="M0 20 Q353 -20 706 20 V54 H0Z" fill="#141414"/></svg>
</section>

<section class="focus">
  <div class="abs bar"></div>
  <h2 class="abs">MEINE<br><span>SCHWERPUNKTE</span></h2>
  <p class="abs lead">Als Ihr externer Marketing Partner biete ich maßgeschneiderte Lösungen, die genau dort ansetzen, wo Sie Unterstützung brauchen.</p>
  <span class="abs link">Jetzt anfragen &nbsp;→</span>
  <div class="abs grid">
    <div class="fcard"><div class="ic"><svg width="18" height="18" fill="none" stroke="#1f8a4c" stroke-width="1.6"><circle cx="9" cy="9" r="7"/><circle cx="9" cy="9" r="3"/></svg></div><h3>Marketing Strategie</h3><p>Entwicklung zielgerichteter Strategien für nachhaltiges Wachstum.</p></div>
    <div class="fcard"><div class="ic"><svg width="18" height="18" fill="none" stroke="#1f8a4c" stroke-width="1.6"><circle cx="9" cy="9" r="7"/><circle cx="6" cy="7" r="1"/><circle cx="11" cy="6" r="1"/></svg></div><h3>Branding</h3><p>Aufbau und Pflege einer starken, unverwechselbaren Marke.</p></div>
    <div class="fcard"><div class="ic"><svg width="18" height="18" fill="none" stroke="#1f8a4c" stroke-width="1.6"><path d="M9 2 L16 6 V12 L9 16 L2 12 V6Z"/></svg></div><h3>Product Management</h3><p>Optimierung Ihres Produktlebenszyklus und Marktpositionierung.</p></div>
    <div class="fcard"><div class="ic"><svg width="18" height="18" fill="none" stroke="#1f8a4c" stroke-width="1.6"><path d="M3 7 V11 H6 L13 15 V3 L6 7Z"/></svg></div><h3>Kommunikation</h3><p>Werbe- und Kommunikationsplanung, die ankommt.</p></div>
    <div class="fcard"><div class="ic"><svg width="18" height="18" fill="none" stroke="#1f8a4c" stroke-width="1.6"><rect x="2" y="3" width="10" height="7" rx="1"/><rect x="6" y="8" width="10" height="7" rx="1"/></svg></div><h3>Beratung</h3><p>Persönliche Beratung und Sparringspartner für Ihre Ideen.</p></div>
    <div class="fcard"><div class="ic"><svg width="18" height="18" fill="none" stroke="#1f8a4c" stroke-width="1.6"><rect x="2" y="3" width="14" height="9" rx="1"/><path d="M9 12 V16 M6 16 H12"/></svg></div><h3>Workshops</h3><p>Events, Workshops und Schulungen für Ihr Team.</p></div>
  </div>
  <svg class="abs wave" width="1200" height="44" viewBox="0 0 1200 44"><path d="M0 24 C300 -8 700 44 1200 20 V44 H0Z" fill="#4f5a53"/><path d="M0 36 C300 10 700 48 1200 30 V44 H0Z" fill="#eef8f3"/></svg>
</section>

<section class="prices">
  <h2 class="abs center">PREISE</h2>
  <div class="abs rule"></div>
  <p class="abs center lead">Transparenz ist mir wichtig. Jede Zusammenarbeit wird individuell offeriert, basierend auf<br>Ihren Bedürfnissen.</p>
  <div class="abs plan light">
    <div class="top"><div><h3>Halbtage</h3><span class="pill">PROJEKTBASIS</span></div><div class="price">580<small>CHF</small></div></div>
    <ul>
      <li><i><svg width="8" height="8" fill="none" stroke="#999" stroke-width="1.6"><path d="M1 4 L3 6 L7 2"/></svg></i>Coaching für spezifische Projekte</li>
      <li><i><svg width="8" height="8" fill="none" stroke="#999" stroke-width="1.6"><path d="M1 4 L3 6 L7 2"/></svg></i>Mitarbeit direkt im Unternehmen</li>
      <li><i><svg width="8" height="8" fill="none" stroke="#999" stroke-width="1.6"><path d="M1 4 L3 6 L7 2"/></svg></i>Lancierung von Produkten</li>
      <li><i><svg width="8" height="8" fill="none" stroke="#999" stroke-width="1.6"><path d="M1 4 L3 6 L7 2"/></svg></i>Relaunch &amp; Marktanalysen</li>
    </ul>
    <span class="cta">OFFERTE ANFRAGEN</span>
  </div>
  <div class="abs plan dark">
    <div class="top"><div><h3>Einzelstunden</h3><span class="pill">FLEXIBEL</span></div><div class="price">160<small>CHF</small></div></div>
    <ul>
      <li><i><svg width="8" height="8" fill="none" stroke="#fff" stroke-width="1.6"><path d="M1 4 L3 6 L7 2"/></svg></i>Erstellen der Marketing Strategie</li>
      <li><i><svg width="8" height="8" fill="none" stroke="#fff" stroke-width="1.6"><path d="M1 4 L3 6 L7 2"/></svg></i>Sortimentsanalysen mit Massnahmen</li>
      <li><i><svg width="8" height="8" fill="none" stroke="#fff" stroke-width="1.6"><path d="M1 4 L3 6 L7 2"/></svg></i>Branding &amp; Social Media Inhalte</li>
      <li><i><svg width="8" height="8" fill="none" stroke="#fff" stroke-width="1.6"><path d="M1 4 L3 6 L7 2"/></svg></i>Website Beratung</li>
    </ul>
    <span class="cta">TERMIN VEREINBAREN</span>
  </div>
</section>

<section class="contact">
  <h2 class="abs">KONTAKT</h2>
  <div class="abs rule"></div>
  <p class="abs lead">Bereit für den nächsten Schritt? Ich freue mich darauf, mit Ihnen zusammenzuarbeiten und Ihr Unternehmen voranzubringen.</p>
  <div class="abs info" style="top:305px"><div class="ic"><svg width="18" height="18" fill="none" stroke="#1f8a4c" stroke-width="1.6"><path d="M9 17 C4 11 3 9 3 7 A6 6 0 0 1 15 7 C15 9 14 11 9 17Z"/><circle cx="9" cy="7" r="2"/></svg></div><div><b>Adresse</b><span>Velorusk, Mirelka Jost GmbH<br>Lindenweg 4, CH-6300 Musterdorf</span></div></div>
  <div class="abs info" style="top:397px"><div class="ic"><svg width="18" height="18" fill="none" stroke="#1f8a4c" stroke-width="1.6"><path d="M3 2 H7 L8 6 L6 7 C7 10 8 11 11 12 L12 10 L16 11 V15 C9 16 2 9 3 2Z"/></svg></div><div><b>Telefon</b><span>+41 79 000 12 34</span></div></div>
  <div class="abs info" style="top:473px"><div class="ic"><svg width="18" height="18" fill="none" stroke="#1f8a4c" stroke-width="1.6"><rect x="2" y="4" width="14" height="10" rx="1"/><path d="M2 5 L9 10 L16 5"/></svg></div><div><b>E-Mail</b><span>info@velorusk.ch</span></div></div>
  <div class="abs me" role="img" aria-label="Porträtfoto der Beraterin"></div>
  <span class="abs soc" style="left:193px;top:603px"></span>
  <span class="abs soc" style="left:240px;top:603px"></span>
  <p class="abs note">„Auf Kontrabu findest du alles über meinen Background"</p>
  <div class="abs form">
    <h3>Schreiben Sie mir</h3>
    <div class="row"><div class="field">Vorname *</div><div class="field">Nachname *</div></div>
    <div class="row"><div class="field">E-Mail Adresse *</div></div>
    <div class="field" style="height:128px">Ihre Nachricht *</div>
    <div class="consent"><i></i><span>Ich stimme zu, dass meine Angaben dauerhaft gespeichert werden. (Datenschutzkonform nach DSG)</span></div>
    <div class="send">➤ &nbsp;Nachricht senden</div>
  </div>
</section>

<footer class="foot">
  <div class="abs logo">velorusk</div>
  <p class="abs about">Velorusk begleitet Schweizer KMUs und Einzelfirmen auf dem Weg zu einer starken Marke und sichtbarem Erfolg. Klar, Inspirierend, Wirksam.</p>
  <div class="abs" style="left:620px;top:76px"><h4>Rechtliches</h4><ul><li>Impressum</li><li>Datenschutzerklärung</li><li>AGB</li></ul></div>
  <div class="abs" style="left:886px;top:76px"><h4>Social Media</h4><div class="socs"><i></i><i></i></div></div>
  <div class="abs base"><span>© 2024 Velorusk, Mirelka Jost GmbH. Alle Rechte vorbehalten.</span><span>Made with <span style="color:var(--green)">♥</span> in Switzerland</span></div>
</footer>

</body>
</html>
```